Can Design for Coconut Water Brand

We want a coconut water can design that is cool and vibrant and tropical feel good appeal that is similar to the uploaded file except less coconut trees and similar colour background. The idea is to make it look colourful but also clean to represent coconut water. We are a small business and just starting out and are planning to sell in Australia and potentially export one day. The idea is to have a can packaging that is bright and attractive to consumers of all ages that are coconut water drinkers or aiming to drink functional beverages instead of soft drinks so the packaging has to stand out amongst all the other coconut water brands in the market.

Target Market(s)

Australia Main Stream

Font styles to use
Decorative

Colors

Designer to choose colors to be used in the design.

Requirements
Must have
• The graphic design must be adjustable to fit 520ml can and 330 ml can as well and it should be ready for editing as once we pick the can design we will add our brand logo on it and also put nutritional facts on it at the same time other print details that need to go on the can. The logo is attached underneath it's called HARBOR GLOW and also pls add 100% Coconut Water on the side of the can and it has to be bold and big enough to be seen or play around and let's see what works best.
Nice to have
• let the designer work their imagination on this

```html
<!DOCTYPE html>
<html lang="en">
<head>
<meta charset="utf-8">
<title>Harbor Glow Coconut Water – Can Label</title>
<link rel="stylesheet" href="https://fonts.googleapis.com/css2?family=Cinzel:wght@500&family=Kaushan+Script&display=swap">
<style>
  :root {
    --page: #eef3f5;
    --teal: #2ec3a6;
    --teal-deep: #22a98f;
    --sun: #f2bb2c;
    --coral: #dd5e5c;
    --coral-deep: #d04f55;
    --white: #ffffff;
  }
  * { box-sizing: border-box; margin: 0; padding: 0; }
  html, body {
    width: 1200px;
    height: 1200px;
    overflow: hidden;
    background: var(--page);
  }
  .canvas {
    position: relative;
    width: 1200px;
    height: 1200px;
    display: flex;
    align-items: center;
    justify-content: center;
  }
  .can-label {
    position: relative;
    width: 620px;
    height: 1080px;
    overflow: hidden;
    background: linear-gradient(180deg,
      var(--teal-deep) 0%,
      var(--teal) 32%,
      #8fc27a 47%,
      var(--sun) 57%,
      #e88d45 70%,
      var(--coral) 82%,
      var(--coral-deep) 100%);
    color: var(--white);
  }
  .palm-art {
    position: absolute;
    background: linear-gradient(180deg, rgba(255,255,255,0.42), rgba(255,255,255,0.22));
  }
  .palm-art--top-left {
    left: 0; top: 100px; width: 170px; height: 380px;
    border-radius: 0 60% 55% 0 / 0 45% 55% 0;
  }
  .palm-art--right-crown {
    right: 0; top: 220px; width: 220px; height: 230px;
    border-radius: 60% 0 0 55% / 55% 0 0 50%;
  }
  .palm-art--right-trunk {
    right: 20px; top: 420px; width: 40px; height: 400px;
    border-radius: 20px;
  }
  .palm-art--bottom-right {
    right: 0; bottom: 0; width: 230px; height: 320px;
    border-radius: 70% 0 0 0 / 60% 0 0 0;
  }

  .brand {
    position: absolute;
    top: 400px;
    left: 0;
    width: 100%;
    display: flex;
    flex-direction: column;
    align-items: center;
    gap: 14px;
  }
  .brand__dot {
    width: 26px;
    height: 26px;
    border-radius: 50%;
    background: var(--white);
  }
  .brand__name {
    font-family: "Cinzel", serif;
    font-weight: 500;
    font-size: 30px;
    line-height: 1;
    letter-spacing: 1px;
    color: var(--white);
  }
  .product-name {
    position: absolute;
    top: 488px;
    left: 0;
    width: 100%;
    text-align: center;
    font-family: "Kaushan Script", cursive;
    font-weight: 400;
    font-size: 128px;
    line-height: 0.98;
    color: var(--white);
    transform: rotate(-4deg);
  }
  .product-name span { display: block; }
  .product-name__second { padding-left: 40px; }
  .swash {
    position: absolute;
    top: 775px;
    left: 200px;
    width: 210px;
    height: 50px;
  }
  .volume {
    position: absolute;
    top: 915px;
    left: 0;
    width: 100%;
    text-align: center;
    font-family: "Kaushan Script", cursive;
    font-size: 60px;
    line-height: 1;
    color: var(--white);
  }
</style>
</head>
<body>
  <main class="canvas">
    <section class="can-label" aria-label="Harbor Glow coconut water can label">
      <div class="palm-art palm-art--top-left" role="img" aria-label="White palm frond silhouettes at the left edge"></div>
      <div class="palm-art palm-art--right-crown" role="img" aria-label="White palm tree crown silhouette"></div>
      <div class="palm-art palm-art--right-trunk" role="img" aria-label="White palm tree trunk silhouette"></div>
      <div class="palm-art palm-art--bottom-right" role="img" aria-label="White palm fronds silhouette at the lower right"></div>

      <div class="brand">
        <span class="brand__dot"></span>
        <p class="brand__name">HARBOR GLOW</p>
      </div>

      <h1 class="product-name">
        <span class="product-name__first">Coconut</span>
        <span class="product-name__second">Water</span>
      </h1>

      <svg class="swash" viewBox="0 0 210 50" aria-hidden="true">
        <path d="M8 40 Q105 12 202 8" fill="none" stroke="var(--white)" stroke-width="11" stroke-linecap="round"/>
      </svg>

      <p class="volume">330ml</p>
    </section>
  </main>
</body>
</html>
```